Cardiology practice business card

We need a business card for our cardiology practice "Wattle Cardiology". We have a new logo, attached below. We like the colours in the logo - red and charcoal. The front of the business card will need to have the doctors name, address, phone number and email. The back will need to have space to write 2 appointment dates and times.

```html
<!DOCTYPE html>
<html lang="en">
<head>
<meta charset="UTF-8">
<title>Wattle Cardiology – Appointment Card</title>
<link rel="stylesheet" href="https://fonts.googleapis.com/css2?family=Montserrat:wght@700&display=swap">
<style>
  :root {
    --charcoal: #262628;
    --heart-red: #c8262d;
    --field-white: #ffffff;
  }
  html, body {
    margin: 0;
    padding: 0;
    overflow: hidden;
    background: var(--charcoal);
  }
  .card {
    position: relative;
    width: 1200px;
    height: 777px;
    background: var(--charcoal);
    overflow: hidden;
    font-family: "Montserrat", Arial, sans-serif;
  }
  .practice-name {
    position: absolute;
    left: 440px;
    top: 150px;
    margin: 0;
    color: var(--heart-red);
    font-weight: 700;
    font-size: 54px;
    letter-spacing: 3px;
    line-height: 1.25;
    text-transform: uppercase;
  }
  .practice-name span { display: block; }
  .appointment-field {
    position: absolute;
    left: 246px;
    width: 709px;
  }
  .appointment-field.date { top: 472px; }
  .appointment-field.time { top: 613px; }
  .field-label {
    display: block;
    margin: 0 0 7px 4px;
    color: var(--heart-red);
    font-weight: 700;
    font-size: 19px;
    letter-spacing: -0.5px;
    line-height: 1;
    text-transform: uppercase;
  }
  .field-box {
    height: 85px;
    background: var(--field-white);
    border-radius: 36px;
  }
</style>
</head>
<body>
  <main class="card">
    <h1 class="practice-name"><span>Wattle</span><span>Cardiology</span></h1>

    <section class="appointment-field date">
      <span class="field-label">Date</span>
      <div class="field-box"></div>
    </section>

    <section class="appointment-field time">
      <span class="field-label">Time</span>
      <div class="field-box"></div>
    </section>
  </main>
</body>
</html>
```